PEACFUL ACUPUNCTURE PRACTITIONER NEEDS A NEW COAT

I need a new design for an exiting website http://willowgateneedlework.com/ for a acupuncturist. This will be a minimalism design with lots and lots of white space. Home page and one interior page. Please keep the feeling of calm and peaceful serenity. For Color scheme: https://www.morningfernclinic.com/fertility. The bottom part of the home page with sections and links to the service pages: https://harborlotuswellness.com/. The client likes this the best: http://mfclinic.com/. I'm attaching the logo and content pages.

Target Market(s)

Women

Industry/Entity Type

Wellness, health, wellbeing, meditation

Number of Pages Required

2 page

Font styles to use
Sans Serif
Decorative

Colors

Designer to choose colors to be used in the design.

Requirements
Must have
Nice to have
• Follow new website drafts and links
Should not have
• Busy with bright colors. No poping

```html
<!DOCTYPE html>
<html lang="en">
<head>
<meta charset="utf-8">
<title>Willowgate Acupuncture</title>
<link href="https://fonts.googleapis.com/css2?family=Mulish:wght@400;500&family=Satisfy&display=swap" rel="stylesheet">
<style>
:root{
  --ink:#3b2a2d;
  --accent:#8a4553;
  --accent-soft:#d9b3bb;
  --btn:#5a2430;
  --band:#fcf0f1;
  --blush:#fdf6f6;
  --rose:#fcedee;
  --rule:#d8cfd1;
  --white:#ffffff;
}
*{margin:0;padding:0;box-sizing:border-box}
html,body{width:764px;height:1200px;overflow:hidden}
body{position:relative;font-family:'Mulish',sans-serif;color:var(--ink);background:var(--white);font-size:7.5px}
.abs{position:absolute}
.script{font-family:'Satisfy',cursive;color:var(--accent)}
.btn{position:absolute;background:var(--btn);color:var(--white);font-size:7px;display:flex;align-items:center;justify-content:center;text-transform:uppercase;letter-spacing:.2px}
.icon-circle{position:absolute;width:21px;height:21px;border-radius:50%;background:#f1dfe2;display:flex;align-items:center;justify-content:center}
.icon-circle svg{width:10px;height:10px;fill:none;stroke:var(--accent);stroke-width:1.4}

/* header */
.top-line{font-size:7.5px;text-transform:uppercase;display:flex;align-items:center;gap:6px}
.top-line span{color:var(--accent);text-transform:none}
.top-line svg{width:12px;height:12px;fill:none;stroke:#777;stroke-width:1.2}
.top-rule{height:1px;background:var(--rule)}
.info{font-size:7.5px;line-height:11.5px}
.brand{position:absolute;left:332px;top:8px;width:100px;text-align:center;color:var(--accent)}
.brand-dot{width:22px;height:22px;border-radius:50%;background:var(--accent-soft);margin:0 auto 4px}
.brand-name{font-size:14px;line-height:14px;color:#6e5a5e}
.brand-sub{font-size:7.5px;letter-spacing:2.2px;color:#6e5a5e}

/* nav */
.nav{position:absolute;left:0;top:74px;width:764px;height:32px;background:var(--band)}
.nav ul{list-style:none;display:flex;justify-content:space-between;margin:0 102px 0 104px;height:32px;align-items:center;font-size:7.5px;text-transform:uppercase}

/* hero */
.hero{position:absolute;left:0;top:106px;width:764px;height:276px;background:linear-gradient(100deg,#e9d8d3 0%,#f0dcd6 30%,#efe2e0 60%,#eadcd9 100%)}
.hero-text h1{font-weight:400;font-size:19px;line-height:24px;color:var(--accent)}
.arrow{position:absolute;width:33px;height:33px;border-radius:50%;background:var(--white);display:flex;align-items:center;justify-content:center}
.arrow svg{width:10px;height:12px;fill:none;stroke:var(--ink);stroke-width:1}

/* philosophy */
.philosophy{position:absolute;left:0;top:382px;width:764px;height:315px;background:var(--blush)}
h2{font-weight:400;font-size:19px;color:var(--accent)}
.copy{font-size:7.5px;line-height:15.2px;width:325px}
.photo{position:absolute}

/* services */
.services{position:absolute;left:0;top:697px;width:764px;height:389px;background:var(--rose)}
.card{position:absolute;top:125px;width:131px;height:205px;background:var(--white)}
.card .photo{left:0;top:0;width:131px;height:92px}
.card h3{position:absolute;left:9px;top:107px;font-weight:400;font-size:11.5px;color:var(--accent)}
.card p{position:absolute;left:10px;top:130px;width:115px;line-height:15px}
.card .btn{left:10px;top:169px;width:64px;height:19px;font-size:6.5px}

/* footer */
.foot-item{position:absolute;top:1115px;display:flex;align-items:center;gap:7px;font-size:7.5px;line-height:11.5px}
.foot-item .icon-circle{position:static}
</style>
</head>
<body>

<header>
  <div class="abs top-line" style="left:102px;top:6px">
    <svg viewBox="0 0 12 12"><path d="M2 1l2 3-1 1c1 2 2 3 4 4l1-1 3 2-1 2C5 11 1 7 1 2z"/></svg>
    Schedule a free 30 minute consultation : <span>413-555-0148</span>
  </div>
  <div class="abs top-rule" style="left:102px;top:24px;width:240px"></div>
  <div class="abs top-line" style="left:424px;top:6px">
    <svg viewBox="0 0 14 12" style="width:18px"><rect x="4" y="2" width="9" height="8"/><path d="M4 2l4.5 4L13 2M0 5h3M1 7h2"/></svg>
    For any questions : <span>ivy@willowgateacupuncture.com</span>
  </div>
  <div class="abs top-rule" style="left:424px;top:24px;width:240px"></div>

  <div class="icon-circle" style="left:149px;top:38px"><svg viewBox="0 0 10 10"><path d="M5 9S2 6 2 4a3 3 0 016 0c0 2-3 5-3 5z"/><circle cx="5" cy="4" r="1"/></svg></div>
  <div class="abs info" style="left:177px;top:37px">14 Alder Row Easthaven,<br>MA 01099 413-555-0148</div>

  <div class="brand">
    <div class="brand-dot"></div>
    <div class="brand-name">Willowgate</div>
    <div class="brand-sub">ACUPUNCTURE</div>
  </div>

  <div class="icon-circle" style="left:483px;top:38px"><svg viewBox="0 0 10 10"><circle cx="5" cy="5" r="4"/><path d="M5 2.5V5h2"/></svg></div>
  <div class="abs info" style="left:511px;top:37px">Tuesday – Friday 10-6<br>Saturday 10-3</div>
</header>

<nav class="nav">
  <ul>
    <li>Home</li><li>About</li><li>Fertility &amp; Pregnancy</li><li>Hormone Balance</li><li>Strength &amp; Structure</li><li>Emotional Wellbeing</li><li>Online Shop</li><li>Testimonials</li>
  </ul>
</nav>

<section class="hero" role="img" aria-label="Practitioner applying moxibustion during an acupuncture treatment, soft blush tones">
  <div class="arrow" style="left:50px;top:121px"><svg viewBox="0 0 10 12"><path d="M7 1L2 6l5 5"/></svg></div>
  <div class="arrow" style="left:681px;top:121px"><svg viewBox="0 0 10 12"><path d="M3 1l5 5-5 5"/></svg></div>
  <div class="abs hero-text" style="left:434px;top:78px">
    <div class="script" style="font-size:19px">Specializing in woman's</div>
    <h1>Health, fertility challenges &amp;<br>pregnancy care</h1>
  </div>
  <div class="btn" style="left:436px;top:170px;width:97px;height:21px">Go to online shop</div>
</section>

<section class="philosophy">
  <div class="abs script" style="left:102px;top:50px;font-size:17px">take care</div>
  <h2 class="abs" style="left:100px;top:77px">Philosophy of Care</h2>
  <p class="abs copy" style="left:102px;top:115px">Acupuncture &amp; Chinese Herbal Medicine are rooted in over 3000 years of history and tradition. As a complete medical system that has remained flexible and relevant we honor what has worked from the past while embracing the medicine of tomorrow.</p>
  <p class="abs copy" style="left:102px;top:176px">At Willowgate Acupuncture we provide compassionate, respectful and empowering care in a safe and inclusive environment. Our goal is to harmonize physical, mental and emotional wellbeing to strengthen the Willowgate from which we all strive to live.</p>
  <div class="btn" style="left:102px;top:235px;width:75px;height:21px">Get in touch</div>
  <div class="photo" role="img" aria-label="Prenatal ultrasound on a pregnant belly" style="left:449px;top:47px;width:214px;height:218px;background:linear-gradient(160deg,#e6e4e6 0%,#d9c3b6 45%,#9fb2c6 80%,#bccbd8 100%)"></div>
</section>

<section class="services">
  <div class="abs script" style="left:0;width:764px;text-align:center;top:54px;font-size:15px">services</div>
  <h2 class="abs" style="left:0;width:764px;text-align:center;top:76px">Area of Focus</h2>

  <article class="card" style="left:102px">
    <div class="photo" role="img" aria-label="Bird nest holding a single blue egg" style="background:linear-gradient(135deg,#5c5242,#8a7a5e,#4e4a3c)"></div>
    <h3>Fertility &amp; Pregnancy</h3>
    <p>At Willowgate Acupuncture our goal is to help build..</p>
    <div class="btn">Read more</div>
  </article>
  <article class="card" style="left:246px">
    <div class="photo" role="img" aria-label="Hands holding a red felt heart against a grey sweater" style="background:linear-gradient(135deg,#8d8d8d,#a9a6a4,#7d7b7a)"></div>
    <h3>Emotional Well Being</h3>
    <p>Our mental and emotional wellness is imperative to..</p>
    <div class="btn">Read more</div>
  </article>
  <article class="card" style="left:390px">
    <div class="photo" role="img" aria-label="Misty blue mountain ridges above rocky peaks" style="background:linear-gradient(180deg,#b9c6cf,#6f8ea4 45%,#4b4c4f)"></div>
    <h3>Hormone Balance</h3>
    <p>Our hormones are constantly shifting and occasionally..</p>
    <div class="btn">Read more</div>
  </article>
  <article class="card" style="left:534px">
    <div class="photo" role="img" aria-label="Old mossy tree with spreading roots in a green forest" style="background:linear-gradient(135deg,#7fa83a,#5d7a2e,#8fb545)"></div>
    <h3>Strength &amp; Structure</h3>
    <p>Our bodies carry us through all we do. Sometimes they need..</p>
    <div class="btn">Read more</div>
  </article>
</section>

<footer>
  <div class="abs" style="left:102px;top:1117px;display:flex;align-items:center;gap:5px">
    <div style="width:24px;height:24px;border-radius:50%;background:var(--accent-soft)"></div>
    <div style="color:#6e5a5e"><div style="font-size:14px;line-height:13px">Willowgate</div><div style="font-size:7.5px;letter-spacing:2.2px">ACUPUNCTURE</div></div>
  </div>
  <div class="foot-item" style="left:241px">
    <div class="icon-circle"><svg viewBox="0 0 10 10"><path d="M5 9S2 6 2 4a3 3 0 016 0c0 2-3 5-3 5z"/><circle cx="5" cy="4" r="1"/></svg></div>
    <div>14 Alder Row Easthaven,<br>MA 01099 413-555-0148</div>
  </div>
  <div class="foot-item" style="left:384px">
    <div class="icon-circle"><svg viewBox="0 0 10 10"><path d="M2 1l1.5 2.5-1 1c1 1.5 2 2.5 3 3l1-1L9 8 8 9.5C4 9 1 6 1 2z"/></svg></div>
    <div>Schdule a Free Consultation:<br>413-555-0148</div>
  </div>
  <div class="foot-item" style="left:518px">
    <div class="icon-circle"><svg viewBox="0 0 10 10"><rect x="1" y="2" width="8" height="6"/><path d="M1 2l4 3.5L9 2"/></svg></div>
    <div>For any Question:<br>ivy@willowgateacupuncture.com</div>
  </div>
  <div class="abs" style="left:102px;top:1173px;width:562px;height:1px;background:var(--rule)"></div>
  <div class="abs" style="left:0;top:1184px;width:764px;text-align:center">Copyright © 2021 Willowgate Acupuncture. All Rights Reserved.</div>
</footer>

</body>
</html>
```